Rapidly growing regional logistics company looking for a modern clean website design.

We need a website for a 5 year old company based in New England.
We offer a complete logistics solution. With services dedicated to the changing economic environment. Services to our customers include, same day delivery, trucking and van service, warehouse & storage, pool distribution, and B2B installations.
We've implemented leading technology along the way, that provides visibility, accountability, up to the minute tracking, and project management.
Our goal to be known in the industry we service as an excellent provider of time-critical services and dependability.
Independently of the services we offer, our customers know that they can count on a true partner.

Target Market(s)

B2B, including printers, retail, manufacturers, wholesalers, electronics, any company that needs product delivered or warehoused

Industry/Entity Type

Logistics

Coding

Coded - Design and coding required

Number of Pages Required

5+ page

Font styles to use
Sans Serif

Colors
0255a3

Requirements
Must have
• Clean, modern design, limited clutter. Limited tabs, preferred everything on 1st screen roll down to see info

```html
<!DOCTYPE html>
<html lang="en">
<head>
<meta charset="utf-8">
<title>Harbor Route Logistics</title>
<link href="https://fonts.googleapis.com/css2?family=Lato:wght@400;700;900&family=Open+Sans:wght@400;600;700&display=swap" rel="stylesheet">
<style>
:root{
  --brand:#0255a3;
  --brand-dark:#013f7a;
  --ink:#2c2c2c;
  --text:#555;
  --grey-bg:#ececec;
  --topbar:#2a2a2a;
  --footer:#303030;
  --footer-deep:#1f1f1f;
  --white:#fff;
}
*{box-sizing:border-box;margin:0;padding:0}
html,body{width:1200px;height:4272px;overflow:hidden}
body{font-family:"Open Sans",sans-serif;color:var(--text);background:var(--white);font-size:14px;line-height:1.6}
h1,h2,h3,h4{font-family:"Lato",sans-serif;color:var(--ink)}
.wrap{width:960px;margin:0 auto;position:relative}
a{color:inherit;text-decoration:none}

.topbar{height:32px;background:var(--topbar);color:#ccc;font-size:11px}
.topbar .wrap{display:flex;justify-content:space-between;align-items:center;height:32px}
.topbar nav span{margin-left:14px}

.header{height:120px}
.header .wrap{display:flex;align-items:center;height:120px}
.logo{display:flex;align-items:center;gap:12px;width:440px}
.logo-dot{width:44px;height:44px;border-radius:50%;background:var(--brand)}
.logo-name{font-family:"Lato",sans-serif;font-weight:900;font-size:24px;color:var(--brand);letter-spacing:1px}
.contact-item{display:flex;align-items:center;gap:8px;margin-right:34px;font-size:12px;color:var(--ink);line-height:1.3}
.contact-item b{display:block;font-size:13px}
.contact-item svg{width:26px;height:26px}
.quote-btn{margin-left:auto;background:var(--brand);color:var(--white);font-family:"Lato",sans-serif;font-weight:700;font-size:13px;padding:12px 20px;border-radius:3px}

.mainnav{height:56px;background:var(--brand)}
.mainnav .wrap{display:flex;height:56px;align-items:center}
.mainnav a{color:var(--white);font-family:"Lato",sans-serif;font-weight:700;font-size:15px;padding:0 24px;height:56px;display:flex;align-items:center}
.mainnav a.active{background:var(--brand-dark)}

.hero{height:532px;position:relative;background:linear-gradient(180deg,#b9cbe0 0%,#d9e2ec 40%,#7f8b99 70%,#b86b34 85%,#3f4d5e 100%);text-align:center;color:var(--white)}
.hero-copy{position:absolute;top:150px;left:0;right:0}
.hero h1{color:var(--white);font-size:46px;font-weight:900;line-height:1.15;letter-spacing:1px;text-transform:uppercase}
.hero p{font-size:14px;margin:12px auto 22px;width:440px}
.btn-outline{display:inline-block;border:1px solid currentColor;padding:8px 26px;font-size:13px;border-radius:3px}
.hero .btn-outline{background:rgba(255,255,255,.2)}
.arrow{position:absolute;top:250px;width:40px;height:40px;border-radius:50%;background:rgba(255,255,255,.85)}
.arrow.left{left:20px}.arrow.right{right:20px}
.dots{height:80px;display:flex;justify-content:center;align-items:center;gap:10px}
.dots i{width:12px;height:12px;border-radius:50%;background:#9a9a9a}
.dots i.on{background:#333}

.section-title{text-align:center;font-size:34px;font-weight:700;color:var(--ink)}
.warehousing{height:540px;padding-top:10px}
.warehousing .lead{text-align:center;width:860px;margin:12px auto 50px;font-size:14px}
.services{display:grid;grid-template-columns:repeat(3,1fr);row-gap:50px;column-gap:40px}
.service{display:flex;gap:16px}
.service-icon{width:50px;height:50px;border-radius:50%;background:var(--brand);flex:none;display:flex;align-items:center;justify-content:center}
.service h3{color:var(--brand);font-size:16px;font-weight:900;text-transform:uppercase}
.service p{font-size:12px;line-height:1.5;margin:4px 0}
.service a{font-size:12px;color:var(--ink);font-weight:600}

.truck{height:640px;background:var(--grey-bg);padding-top:60px}
.truck .wrap{display:flex;justify-content:space-between}
.truck-copy{width:420px}
.truck h2{font-size:34px;font-weight:700}
.truck .intro{margin:10px 0 18px}
.checklist{list-style:none}
.checklist li{display:flex;gap:12px;align-items:flex-start;margin-bottom:10px;font-size:13px}
.checklist svg{flex:none;width:18px;height:18px;margin-top:2px}
.truck .btn-outline{color:var(--brand);margin-top:10px}
.van-photo{width:500px;height:360px;margin-top:40px;background:radial-gradient(ellipse at 55% 55%,#ffffff 0%,#eef1f5 45%,#cfd6de 75%,var(--grey-bg) 100%)}

.distribution{height:620px;background:linear-gradient(180deg,#2a6cb3,#0255a3 60%,#0a4a8c);color:var(--white);text-align:center;padding-top:60px}
.distribution h2{color:var(--white);font-size:34px;font-weight:700}
.distribution .sub{font-size:15px;margin-bottom:30px}
.distribution p{width:860px;margin:0 auto 22px;font-size:13px;line-height:1.75}
.distribution .btn-outline{margin-top:14px;background:var(--white);color:var(--brand);border-color:var(--white)}

.split{position:relative}
.split .wrap{display:flex;justify-content:space-between;align-items:flex-start}
.split-copy{width:440px}
.split h2{font-size:30px;font-weight:700;margin-bottom:14px}
.split p{font-size:13px;margin-bottom:16px;line-height:1.7}
.split .btn-outline{color:var(--brand)}
.sameday{height:600px;padding-top:60px}
.dedicated{height:580px;background:var(--grey-bg);padding-top:40px}
.photo-sameday{width:440px;height:320px;margin-top:20px;background:linear-gradient(135deg,#9fcf7a,#dfeccd 55%,#8ea1b3)}
.photo-dedicated{width:440px;height:460px;background:linear-gradient(160deg,#4f7fb8,#9ab4d0 45%,#c9a77d 80%,#8a6b45)}

.newsletter{height:160px;background:var(--brand);text-align:center;color:var(--white);padding-top:30px}
.newsletter h2{color:var(--white);font-size:22px;font-weight:900;letter-spacing:1px}
.newsletter .sub{font-size:12px;letter-spacing:1px;text-transform:uppercase}
.subscribe{display:flex;justify-content:center;margin-top:14px}
.subscribe span{width:300px;height:34px;background:var(--white)}
.subscribe b{height:34px;padding:0 22px;background:var(--brand-dark);font-family:"Lato",sans-serif;font-size:13px;line-height:34px}

.footer{height:260px;background:var(--footer);color:#bbb;padding-top:26px;font-size:12px}
.footer .wrap{display:flex;gap:60px}
.footer h4{color:var(--white);font-size:14px;margin-bottom:10px;text-transform:uppercase}
.f-about{width:330px}
.f-about p{margin-bottom:8px;line-height:1.6}
.f-links{width:200px}
.f-links li,.f-office li{list-style:none;margin-bottom:4px}
.f-links li::before{content:"› ";color:var(--white)}
.bottombar{height:52px;background:var(--footer-deep);color:#999;font-size:12px}
.bottombar .wrap{display:flex;justify-content:space-between;align-items:center;height:52px}
.socials{display:flex;gap:8px}
.socials i{width:24px;height:24px;border-radius:50%;border:1px solid #888}
</style>
</head>
<body>

<div class="topbar"><div class="wrap">
  <span>info@harborroute-mail.com</span>
  <nav><span>Default Website</span><span>My Account</span><span>Checkout</span><span>Log In</span><span>English</span><span>USD</span></nav>
</div></div>

<header class="header"><div class="wrap">
  <div class="logo"><span class="logo-dot"></span><span class="logo-name">HARBOR ROUTE</span></div>
  <div class="contact-item">
    <svg viewBox="0 0 24 24"><circle cx="12" cy="12" r="12" fill="#0255a3"/><path d="M8 6l2 0 1 3-1.5 1a7 7 0 0 0 4 4l1-1.5 3 1v2a1 1 0 0 1-1 1A11 11 0 0 1 7 7a1 1 0 0 1 1-1z" fill="#fff"/></svg>
    <div><b>+1 555 014 22 90</b>info@harborroute-mail.com</div>
  </div>
  <div class="contact-item">
    <svg viewBox="0 0 24 24"><circle cx="12" cy="12" r="12" fill="#0255a3"/><circle cx="12" cy="12" r="6" fill="none" stroke="#fff" stroke-width="1.6"/><path d="M12 9v3l2 1.5" stroke="#fff" stroke-width="1.6" fill="none"/></svg>
    <div><b>Mon-Sat 9:00AM-6:00PM</b>Opening Time</div>
  </div>
  <a class="quote-btn" href="#">GET A QUOTE</a>
</div></header>

<nav class="mainnav"><div class="wrap">
  <a class="active" href="#">Home</a><a href="#">Features</a><a href="#">Services ▾</a><a href="#">About Us</a><a href="#">News</a><a href="#">Contact Us</a>
</div></nav>

<section class="hero" role="img" aria-label="Cargo plane over a container port with cranes and stacked shipping containers">
  <span class="arrow left"></span><span class="arrow right"></span>
  <div class="hero-copy">
    <h1>We fright to all over<br>ther world</h1>
    <p>Lorem Ipsum is simply dummy text of the printing and typesetting industry.</p>
    <a class="btn-outline" href="#">Read More</a>
  </div>
</section>
<div class="dots"><i class="on"></i><i></i><i></i><i></i></div>

<section class="warehousing"><div class="wrap">
  <h2 class="section-title">Warehousing</h2>
  <p class="lead">Our warehouse facility may prove to be one of the most valuable extensions of your company's operations. With a secure warehouse conveniently located in central New England we supplement your firm's storage and distribution needs.</p>
  <div class="services">
    <div class="service"><span class="service-icon"><svg width="26" height="20" viewBox="0 0 26 20"><rect x="1" y="3" width="15" height="11" fill="#fff"/><path d="M16 7h5l4 4v3h-9z" fill="#fff"/><circle cx="6" cy="16" r="2.5" fill="#fff"/><circle cx="20" cy="16" r="2.5" fill="#fff"/></svg></span><div><h3>Trucking</h3><p>Lorem Ipsum is simply dummy text of the printing and typesetting and type set since the 1500s</p><a href="#">Read More..</a></div></div>
    <div class="service"><span class="service-icon"><svg width="26" height="20" viewBox="0 0 26 20"><path d="M1 4h16l5 5v6H1z" fill="#fff"/><circle cx="6" cy="16" r="2.5" fill="#fff"/><circle cx="18" cy="16" r="2.5" fill="#fff"/></svg></span><div><h3>Van Service</h3><p>Lorem Ipsum is simply dummy text of the printing and typesetting and type set since the 1500s</p><a href="#">Read More..</a></div></div>
    <div class="service"><span class="service-icon"><svg width="24" height="22" viewBox="0 0 24 22"><path d="M2 8l10-6 10 6v13H2z" fill="#fff"/><rect x="7" y="12" width="10" height="9" fill="#0255a3"/></svg></span><div><h3>Warehouse</h3><p>Lorem Ipsum is simply dummy text of the printing and typesetting and type set since the 1500s</p><a href="#">Read More..</a></div></div>
    <div class="service"><span class="service-icon"><svg width="24" height="22" viewBox="0 0 24 22"><rect x="2" y="2" width="9" height="8" fill="#fff"/><rect x="13" y="2" width="9" height="8" fill="#fff"/><rect x="2" y="12" width="9" height="8" fill="#fff"/><rect x="13" y="12" width="9" height="8" fill="#fff"/></svg></span><div><h3>Storage</h3><p>Lorem Ipsum is simply dummy text of the printing and typesetting and type set since the 1500s</p><a href="#">Read More..</a></div></div>
    <div class="service"><span class="service-icon"><svg width="24" height="22" viewBox="0 0 24 22"><circle cx="12" cy="4" r="3" fill="#fff"/><circle cx="4" cy="18" r="3" fill="#fff"/><circle cx="20" cy="18" r="3" fill="#fff"/><path d="M12 4L4 18M12 4l8 14" stroke="#fff" stroke-width="2"/></svg></span><div><h3>Pool Distribution</h3><p>Lorem Ipsum is simply dummy text of the printing and typesetting and type set since the 1500s</p><a href="#">Read More..</a></div></div>
    <div class="service"><span class="service-icon"><svg width="24" height="22" viewBox="0 0 24 22"><path d="M3 18l9-9 3 3-9 9H3z" fill="#fff"/><circle cx="17" cy="6" r="4" fill="none" stroke="#fff" stroke-width="2.5"/></svg></span><div><h3>B2B Installations:</h3><p>Lorem Ipsum is simply dummy text of the printing and typesetting and type set since the 1500s</p><a href="#">Read More..</a></div></div>
  </div>
</div></section>

<section class="truck"><div class="wrap">
  <div class="truck-copy">
    <h2>Truck &amp; Van Service</h2>
    <p class="intro">Trucking, vehicle and ground transportation include:</p>
    <ul class="checklist">
      <li><svg viewBox="0 0 18 18"><rect x=".5" y=".5" width="17" height="17" fill="#fff" stroke="#0255a3"/><path d="M4 9l3 3 7-7" stroke="#0255a3" stroke-width="2" fill="none"/></svg>Rush and pre-scheduled delivery</li>
      <li><svg viewBox="0 0 18 18"><rect x=".5" y=".5" width="17" height="17" fill="#fff" stroke="#0255a3"/><path d="M4 9l3 3 7-7" stroke="#0255a3" stroke-width="2" fill="none"/></svg>Light and heavy trucking (cargo vans to liftgates)</li>
      <li><svg viewBox="0 0 18 18"><rect x=".5" y=".5" width="17" height="17" fill="#fff" stroke="#0255a3"/><path d="M4 9l3 3 7-7" stroke="#0255a3" stroke-width="2" fill="none"/></svg>Line haul from pick up locations to airports and other designated locations</li>
      <li><svg viewBox="0 0 18 18"><rect x=".5" y=".5" width="17" height="17" fill="#fff" stroke="#0255a3"/><path d="M4 9l3 3 7-7" stroke="#0255a3" stroke-width="2" fill="none"/></svg>Expedited ground services</li>
      <li><svg viewBox="0 0 18 18"><rect x=".5" y=".5" width="17" height="17" fill="#fff" stroke="#0255a3"/><path d="M4 9l3 3 7-7" stroke="#0255a3" stroke-width="2" fill="none"/></svg>LTL (Less than Truckload)</li>
      <li><svg viewBox="0 0 18 18"><rect x=".5" y=".5" width="17" height="17" fill="#fff" stroke="#0255a3"/><path d="M4 9l3 3 7-7" stroke="#0255a3" stroke-width="2" fill="none"/></svg>Late night delivery – we are open 24 hours per day, 365 days per year</li>
      <li><svg viewBox="0 0 18 18"><rect x=".5" y=".5" width="17" height="17" fill="#fff" stroke="#0255a3"/><path d="M4 9l3 3 7-7" stroke="#0255a3" stroke-width="2" fill="none"/></svg>Truckload</li>
    </ul>
    <a class="btn-outline" href="#">Read More</a>
  </div>
  <div class="van-photo" role="img" aria-label="White box delivery van with company lettering on its side"></div>
</div></section>

<section class="distribution"><div class="wrap">
  <h2>Distribution &amp; Pool Services</h2>
  <p class="sub">Our business model is flexible, and it enables us to scale our fleet size to adjust to shipment volume</p>
  <p>Pool Distribution is the distribution of product to numerous customers within a particular geographic region. This is a highly superior and cost-effective alternative to the higher cost of LTL shipments. In some instances, this could represent a 30%-70% savings vs. traditional LTL. Instead of LTL direct to customer, product is shipped to the regional warehouse in truckload quantities. There it is off loaded, then segregated and sorted by customer and then reloaded on local delivery trucks. Pool Distribution reduces transit times, reduces claims and damages and allows for significant savings over LTL rates.</p>
  <p>Product is scanned off the trailer when first received at the regional warehouse; products are scanned and then scanned on delivery.</p>
  <p>Contributing to the cost effectiveness of Pool Distribution over LTL includes: the number of pool points per pool (i.e. # of stores), volumes per store, weight per shipment, frequency of deliveries, and distance from customer to the regional warehouse.</p>
  <a class="btn-outline" href="#">Read More</a>
</div></section>

<section class="split sameday"><div class="wrap">
  <div class="split-copy">
    <h2>Same-day Delivery Service</h2>
    <p>Regardless of the specifics of your needs, Harbor Route can handle your same-day delivery needs. Harbor Route offers same day delivery services as a standalone service or in support of our other services. Our warehousing services, pool distribution, B2B services all rely on our same day service.</p>
    <p>Our on-demand same day shipping is totally customizable to each customer. Each client has their requirements, and we cater to individual customer request. We customize our same day delivery services and on demand shipping solutions so that our clients can gain a competitive advantage while reducing their cost.</p>
    <a class="btn-outline" href="#">Read More</a>
  </div>
  <div class="photo-sameday" role="img" aria-label="Courier handing over a parcel at a doorway"></div>
</div></section>

<section class="split dedicated"><div class="wrap">
  <div class="photo-dedicated" role="img" aria-label="Delivery worker with a clipboard beside stacked cardboard boxes"></div>
  <div class="split-copy" style="margin-top:30px">
    <h2>Dedicated Delivery Service</h2>
    <p>Regardless of the specifics of your needs, Harbor Route can handle your same-day delivery needs. Harbor Route offers same day delivery services as a standalone service or in support of our other services. Our warehousing services, pool distribution, B2B services all rely on our same day service.</p>
    <p>Our on-demand same day shipping is totally customizable to each customer. Each client has their requirements, and we cater to individual customer request. We customize our same day delivery services and on demand shipping solutions so that our clients can gain a competitive advantage while reducing their cost.</p>
    <a class="btn-outline" href="#">Read More</a>
  </div>
</div></section>

<section class="newsletter">
  <h2>SUBSCRIBE TO OUR NEWSLETTER</h2>
  <p class="sub">To receive the latest news &amp; update</p>
  <div class="subscribe"><span></span><b>SUBMIT</b></div>
</section>

<footer class="footer"><div class="wrap">
  <div class="f-about">
    <h4>About Us</h4>
    <p>Our company was founded in 2012 but our team is seasoned, with a combined 75 years of experience.</p>
    <p>Harbor Route offers a complete logistics solution. With services dedicated to</p>
    <p style="color:#fff">READ MORE...</p>
  </div>
  <ul class="f-links">
    <h4>Quick Links</h4>
    <li>Home</li><li>Features</li><li>Services</li><li>About Us</li><li>News</li><li>Contact</li>
  </ul>
  <ul class="f-office">
    <h4>Transport Office</h4>
    <li>1234, Your Full Address</li>
    <li>+1 555 014 22 90</li>
    <li>hello@harborroute-mail.com</li>
    <li>Mon-Sat 9:00am-6:00pm</li>
  </ul>
</div></footer>
<div class="bottombar"><div class="wrap">
  <span>© 2017 Harbor Route – All Rights Reserved</span>
  <div class="socials"><i></i><i></i><i></i><i></i><i></i><i></i></div>
</div></div>

</body>
</html>
```